依頼詳細
人生100年時代・老後2000万円問題の解決に関するセミナーを行いたいと思っており、メインターゲット層はシニア(富裕層)で若年層までと考えております。開催日程は追記します。チラシ配布は5回、セミナー開催は10回(各チラシ2日程を載せる)を予定しています。
初めての取り組みであり、全くの素人なのでアドバイスや一歩先のご提案をいただけると助かります。
記載項目
会社ロゴ、電話番号、https://www.komo-ast.jp/、裏面は添付PDFの文章が必要となります。
サイズ
A4
ページ数
両面
希望イメージ
シンプル 複雑
単色 カラフル
暗い 明るい
日常 高級
遊び心 厳粛
未来的 伝統的
女性的 男性的
希望する色
赤系、茶系
納品ファイル
• 高解像度JPG (.jpg)
• イラストレーター形式 (.ai)
• PNG形式 (.png)
補足説明
日程・写真等をこちらで編集したいので、編集できるファイルが欲しいです。
補足事項を追記させていただきます。
翠嶺証券のアドバイザーであることがわかるようにロゴを入れていただき、「関東財務局長(金商)第736号」を入れていただきたいです。
また裏面のIFAの説明、ヒアリングからフォローまでの流れのデザインを変更、
翠嶺証券の住所が「東京都港区北白浜4-3-17」に変更になっておりますので修正をお願い致します。
修正部分を写真でアップロードさせていただきます。
金融商品仲介業者:株式会社こもれびアセット 登録番号:近畿財務局長(金仲)第512号/所属金融商品取引業者:翠嶺証券株式会社/登録番号:関東財務局長(金商)第736号 加入協会:全国債券取扱連盟、一般社団法人 資産期約取扱者連盟、全国物産期約売買連盟、一般社団法人 小口運用資産取扱者連絡会、一般社団法人 全国資産助言者連盟
当社は所属金融商品取引業者の代理権はありません。当社は金融商品仲介業務に関し、お客様から金銭や有価証券を直接お預かりすることはありません。
セミナー参加者の方へ、商品の勧誘を行うことがあります。商品等にご投資いただく場合には所定の手数料や諸経費等をご負担いただく場合があります。
また、各商品等には相場の変動等による損失が生じる恐れがあります。各商品等へのご投資にかかる手数料およびリスクについては、当該商品等の契約締結前交付書面等をよくお読みになり内容について十分にご理解ください。
※個人情報の取り扱いについて、本セミナーは株式会社こもれびアセットにより運営されており、個人情報は弊社で管理いたします。ご記入いただきましたお客様の個人情報は弊社の利用目的の範囲内で利用させていただきます。

デザイン・修正依頼の対応の速さ・正確さ・丁寧さに非常に満足できました。

デザイン力、修正依頼の対応の早さや正確さ、丁寧さに非常に満足できました。
また機会がありましたらその他のものも依頼したいと思っております。
この度はありがとうございました。

```html
<!DOCTYPE html>
<html lang="ja">
<head>
<meta charset="utf-8">
<title>老後2000万円問題に備える セミナー</title>
<link href="https://fonts.googleapis.com/css2?family=Noto+Serif+JP:wght@400;600;700;900&display=swap" rel="stylesheet">
<style>
  :root{
    --red:#c4161c;
    --deep-red:#a8141a;
    --ink:#222222;
    --sub:#444444;
    --rule:#c9c9c9;
    --paper:#ffffff;
  }
  *{box-sizing:border-box;margin:0;padding:0}
  html,body{width:846px;height:1200px;overflow:hidden;background:var(--paper)}
  body{font-family:"Noto Serif JP",serif;color:var(--ink);position:relative}
  .flyer{position:relative;width:846px;height:1200px;overflow:hidden}

  .top-band{position:absolute;left:0;top:0;width:846px;height:58px;background:var(--red);
    color:#fff;font-weight:700;font-size:27px;letter-spacing:2px;display:flex;align-items:center;padding-left:40px}

  .headline{position:absolute;left:78px;top:110px;display:flex;align-items:center;font-weight:900;font-size:58px;letter-spacing:1px}
  .headline .mark{background:var(--red);color:#fff;padding:4px 10px;line-height:1.15}
  .headline .rest{color:var(--ink);margin-left:4px}
  .headline-rule{position:absolute;left:70px;top:204px;width:706px;height:2px;background:var(--rule)}

  .lead{position:absolute;left:70px;top:232px;font-size:25px;font-weight:700;letter-spacing:1px}

  .topics{position:absolute;left:70px;top:288px;width:720px;display:grid;grid-template-columns:repeat(3,1fr);column-gap:38px;row-gap:30px}
  .topic h3{font-size:20px;font-weight:700;color:var(--deep-red);padding-bottom:4px;border-bottom:1px solid var(--rule);margin-bottom:8px}
  .topic p{font-size:14px;line-height:1.6;color:var(--sub)}

  .back-note{position:absolute;left:395px;top:652px;width:451px;height:40px;background:var(--red);color:#fff;
    font-size:20px;font-weight:700;display:flex;align-items:center;padding-left:22px;letter-spacing:1px}

  .date{position:absolute;left:70px;top:720px;font-size:42px;font-weight:900;color:var(--red);letter-spacing:1px}
  .capacity{position:absolute;left:70px;top:784px;font-size:30px;font-weight:700;color:var(--red)}
  .capacity .num{font-size:34px;margin:0 6px}
  .covid{position:absolute;left:70px;top:836px;font-size:23px;font-weight:700;color:var(--red)}
  .covid-rule{position:absolute;left:70px;top:876px;width:706px;height:2px;background:var(--rule)}

  .photos{position:absolute;left:0;top:898px;width:846px;height:302px;display:grid;grid-template-columns:repeat(3,1fr);gap:10px}
  .photo{height:100%}
  .photo.shield{background:linear-gradient(160deg,#eef0f3,#c9ced6)}
  .photo.thermo{background:linear-gradient(160deg,#f4f4f4,#bfbfbf)}
  .photo.hands{background:linear-gradient(160deg,#e9eef2,#b8c2cc)}
</style>
</head>
<body>
<main class="flyer">
  <div class="top-band">あなたは大丈夫？　みんなやってる？</div>

  <h1 class="headline"><span class="mark">老後2000万円問題</span><span class="rest">に備える</span></h1>
  <div class="headline-rule"></div>

  <p class="lead">人生100年時代の資産運用と保険について！</p>

  <section class="topics">
    <div class="topic"><h3>資産運用</h3><p>翠嶺証券の商品から<br>お客様最適な提案</p></div>
    <div class="topic"><h3>生命保険</h3><p>万が一の保障を<br>必要な方だけ</p></div>
    <div class="topic"><h3>火災保険</h3><p>地震・自然災害にも<br>対応してますか？</p></div>
    <div class="topic"><h3>つみたてNISA</h3><p>積立手数料0円<br>運用益が非課税</p></div>
    <div class="topic"><h3>医療保険</h3><p>長生き時代に合った<br>医療保障</p></div>
    <div class="topic"><h3>自動車保険</h3><p>保険料は保険会社で<br>結構違います！</p></div>
    <div class="topic"><h3>確定拠出年金</h3><p>（iDeCo 個人型）<br>運用益が非課税<br>掛金全額が所得控除</p></div>
    <div class="topic"><h3>相続対策</h3><p>“争続”対策<br>できてますか？</p></div>
    <div class="topic"><h3>ペット保険</h3><p>大切な家族の治療を<br>あきらめないために</p></div>
  </section>

  <div class="back-note">株式会社こもれびアセットの紹介は裏面</div>

  <p class="date">開催日時：2020年12月12日（土）</p>
  <p class="capacity">※他社も含めて個別セミナー<span class="num">3</span>名まで</p>
  <p class="covid">コロナ対策を実施しております。</p>
  <div class="covid-rule"></div>

  <section class="photos">
    <div class="photo shield" role="img" aria-label="フェイスシールドとマスクを着用したスタッフの写真"></div>
    <div class="photo thermo" role="img" aria-label="入口に設置された検温カメラの写真"></div>
    <div class="photo hands" role="img" aria-label="手指を消毒している様子の写真"></div>
  </section>
</main>
</body>
</html>
```